Liquor Label / Aguardiente

Label design for liquor bottle. Designers may submit multiple submissions.

Product Description:
Name: Viento de Plata™
Alcohol Category: Aguardiente (which in Spanish most closely translates to “burning water”) – aguardiente is derived from
cane sugar and is a general term for a type of alcoholic spirit in many Central and South America countries.
Taste: A smooth liquor with a comfortable yet spicy finish
Smell: Subtle aroma of spicy jalapeños
Liquid Color: Clear
Bottle Color: Clear
See link for reference - http://www.kelvostamp.com/sites/default/files/styles/uc_product_full/public/Pemrow_0.jpg?itok=9QmT2xLp
Closure: Bar top / cork
Bottle Shape/Size: height = 8.67in; diameter of base = 3.70in; diameter of neck = 0.85in

Label may consist of two separate parts (i.e. front and back, front and vertical side), or one continuous label.

Designer has complete freedom with color, font etc. unless otherwise stated below. The label MUST
contain (but is not limited only to) the following text exactly as written in quotes below:
- “Viento de Plata”
- “Aguardiente”
- “Cane Neutral Spirit with Natural Flavors”
- “35% Alc./Vol.”
- “750 ml”
- “Bottled by WP Spirits, LLC” and “Nashville, TN” - “Government Warning: (1) According to the Surgeon General, women should not drink alcoholic beverages during
pregnancy because of the risk of birth defects. (2) Consumption of alcoholic beverages impairs your ability to
drive a car or operate machinery, and may cause health problems.” (text in previous quotes must be in all
capitalized letters, text must be 2 MM in height and quote must be separated 2MM by all other text)
- Must be dedicated empty space for bar code (approximately 0.75in. height x 1.25in. length)

Target Market(s)

Label should have mass market appeal.
Age: 21 – 28 years old (primary target market is 21+ year old college students and recent graduates)
Target Market Gender: Both male and female, with emphasis on male
Consumption Focus: Spirit will be consumed typically as a shot, primarily at bars and secondarily off premise (label design will be critical for making our product highly visible behind a bar)
Marketing Theme: South American elements. The official Viento de Plata mascot is a llama and the incorporation and use of a llama somewhere (however large or small) on the bottle is encourage but by no means required.

Industry/Entity Type

Health

Requirements
Should not have
• Elements that may lead a potential consumer to believe the beverage is a craft liquor or an artisan brand. Please do not include images of peppers.

```html
<!DOCTYPE html>
<html lang="en">
<head>
<meta charset="utf-8">
<title>Viento de Plata — Aguardiente Label</title>
<link rel="stylesheet" href="https://fonts.googleapis.com/css2?family=Jost:wght@400;700&family=Italianno&display=swap">
<style>
  :root {
    --page: #ffffff;
    --label: #231f20;
    --ink: #ffffff;
    --tone-green: #4f5a3a;
    --tone-yellow: #fdb913;
    --tone-red: #c03127;
  }
  html, body {
    margin: 0;
    padding: 0;
    width: 951px;
    height: 1200px;
    overflow: hidden;
    background: var(--page);
  }
  .canvas {
    position: relative;
    width: 951px;
    height: 1200px;
  }
  .label {
    position: absolute;
    left: 196px;
    top: 166px;
    width: 558px;
    height: 864px;
    background: var(--label);
    box-shadow: 0 4px 10px rgba(0, 0, 0, 0.22);
    color: var(--ink);
    font-family: "Jost", "Futura", sans-serif;
    overflow: hidden;
  }
  .artwork {
    position: absolute;
    left: 72px;
    top: 189px;
    width: 410px;
    height: 299px;
    background: linear-gradient(90deg, var(--tone-green) 0%, var(--tone-yellow) 50%, var(--tone-red) 100%);
  }
  .brand-name {
    position: absolute;
    left: 0;
    width: 100%;
    top: 42px;
    margin: 0;
    text-align: center;
    font-family: "Italianno", cursive;
    font-weight: 400;
    font-size: 110px;
    line-height: 1;
    color: var(--ink);
    white-space: nowrap;
  }
  .category {
    position: absolute;
    left: 0;
    width: 100%;
    top: 518px;
    margin: 0;
    text-align: center;
    font-weight: 700;
    font-size: 50px;
    letter-spacing: 3px;
    line-height: 1;
  }
  .spirit-type {
    position: absolute;
    left: 0;
    width: 100%;
    top: 627px;
    margin: 0;
    text-align: center;
    font-weight: 400;
    line-height: 1;
  }
  .spirit-type .main { display: block; font-size: 34px; }
  .spirit-type .sub { display: block; font-size: 29px; margin-top: 12px; }
  .abv, .volume {
    position: absolute;
    left: 0;
    width: 100%;
    margin: 0;
    text-align: center;
    font-size: 26px;
    line-height: 1;
  }
  .abv { top: 764px; }
  .volume { top: 818px; }
</style>
</head>
<body>
  <main class="canvas">
    <section class="label">
      <div class="artwork" role="img" aria-label="Brand artwork in green, yellow and red"></div>
      <h1 class="brand-name">Viento de Plata</h1>
      <p class="category">AGUARDIENTE</p>
      <p class="spirit-type">
        <span class="main">CANE NEUTRAL SPIRIT</span>
        <span class="sub">WITH NATURAL FLAVORS</span>
      </p>
      <p class="abv">35% ALC./VOL</p>
      <p class="volume">750 ML</p>
    </section>
  </main>
</body>
</html>
```